Business Card for TVK, logo files already created

Please, can you assist with creating a Business card the TVK graphics which are already listed on www.brinmoretech.example
The business card should be modern and upmarket, textured designs are welcome. Please feel free to express yourself and be very bold with your design.

Target Market(s)

Cyber Security

Industry/Entity Type

Information Technology

Contact Information for Business Card

Company Name
Name
Title
Mobile
Fax or Tel
email
url

Font styles to use
Serif
Sans Serif

Colors
3277b5
85acd3
ffffff

```html
<!DOCTYPE html>
<html lang="en">
<head>
<meta charset="utf-8">
<title>TVK Business Card</title>
<link href="https://fonts.googleapis.com/css2?family=Maven+Pro:wght@400;500;700&display=swap" rel="stylesheet">
<style>
  :root {
    --blue: #3277b5;
    --blue-light: #85acd3;
    --white: #ffffff;
    --card: #282626;
    --card-mark: #1d1c1c;
    --backdrop: #3a3a3a;
  }
  * { margin: 0; padding: 0; box-sizing: border-box; }
  html, body { width: 1200px; height: 900px; overflow: hidden; }
  body {
    background: var(--backdrop);
    font-family: "Maven Pro", sans-serif;
    position: relative;
  }
  .card {
    position: absolute;
    left: 250px;
    width: 700px;
    height: 400px;
    background: var(--card);
    box-shadow: 0 12px 30px rgba(0,0,0,0.45);
  }
  .card-front { top: 40px; }
  .card-back { top: 470px; }

  /* front */
  .front-lockup {
    position: absolute;
    left: 56px;
    top: 250px;
  }
  .company-name {
    color: var(--blue);
    font-weight: 700;
    font-size: 25px;
    letter-spacing: 1.5px;
    text-transform: uppercase;
    white-space: nowrap;
  }
  .tagline {
    color: var(--blue);
    font-weight: 500;
    font-size: 13px;
    letter-spacing: 1.6px;
    text-transform: uppercase;
    margin-top: 6px;
    white-space: nowrap;
  }
  .front-mark {
    position: absolute;
    right: 50px;
    top: 90px;
    color: var(--card-mark);
    font-weight: 700;
    font-size: 120px;
    letter-spacing: 4px;
    line-height: 1;
  }

  /* back */
  .back-lockup {
    position: absolute;
    left: 40px;
    top: 36px;
  }
  .back-lockup .brand-initials {
    color: var(--blue);
    font-weight: 700;
    font-size: 62px;
    line-height: 1;
    letter-spacing: 2px;
  }
  .back-lockup .company-name { font-size: 22px; margin-top: 2px; }
  .back-lockup .tagline { font-size: 11.5px; margin-top: 4px; }

  .divider {
    position: absolute;
    left: 40px;
    right: 40px;
    top: 200px;
    height: 1px;
    background: var(--blue);
  }
  .contact-list {
    position: absolute;
    left: 40px;
    top: 222px;
    list-style: none;
  }
  .contact-list li {
    display: flex;
    align-items: center;
    gap: 14px;
    color: var(--white);
    font-size: 19px;
    height: 32px;
    white-space: nowrap;
  }
  .contact-list svg { width: 20px; height: 20px; fill: var(--blue); flex: none; }
  .person {
    position: absolute;
    right: 40px;
    top: 222px;
    text-align: right;
  }
  .person-name {
    color: var(--blue);
    font-size: 30px;
    font-weight: 500;
    letter-spacing: 0.5px;
  }
  .person-title { color: var(--white); font-size: 16px; margin-top: 2px; }
</style>
</head>
<body>

<section class="card card-front">
  <div class="front-mark">TVK</div>
  <div class="front-lockup">
    <div class="company-name">Brinmore Technologies</div>
    <div class="tagline">Precision - Focused Defense</div>
  </div>
</section>

<section class="card card-back">
  <div class="back-lockup">
    <div class="brand-initials">TVK</div>
    <div class="company-name">Brinmore Technologies</div>
    <div class="tagline">Precision - Focused Defense</div>
  </div>

  <div class="divider"></div>

  <ul class="contact-list">
    <li>
      <svg viewBox="0 0 24 24" aria-hidden="true"><path d="M6.6 10.8c1.4 2.8 3.8 5.1 6.6 6.6l2.2-2.2c.3-.3.7-.4 1-.2 1.1.4 2.3.6 3.6.6.6 0 1 .4 1 1V20c0 .6-.4 1-1 1C10.6 21 3 13.4 3 4c0-.6.4-1 1-1h3.5c.6 0 1 .4 1 1 0 1.3.2 2.5.6 3.6.1.3 0 .7-.2 1L6.6 10.8z"/></svg>
      800 - 555 - 0146
    </li>
    <li>
      <svg viewBox="0 0 24 24" aria-hidden="true"><path d="M7 2h9v5H7zM4 8h16a2 2 0 0 1 2 2v10a2 2 0 0 1-2 2H4a2 2 0 0 1-2-2V10a2 2 0 0 1 2-2zm3 4v2h5v-2zm8 0v2h3v-2zm-8 4v2h5v-2zm8 0v2h3v-2z"/></svg>
      800 - 555 - 0155
    </li>
    <li>
      <svg viewBox="0 0 24 24" aria-hidden="true"><path d="M2 5h20v14H2zm2 2v.5l8 5.5 8-5.5V7l-8 5.5z"/></svg>
      contact@brinmoretech.example
    </li>
    <li>
      <svg viewBox="0 0 24 24" aria-hidden="true"><path d="M12 2a10 10 0 1 0 0 20 10 10 0 0 0 0-20zm-1 17.9A8 8 0 0 1 4.1 10H7l2 2v2l2 2zm6.9-2.5c-.3-.8-1-1.4-1.9-1.4h-1v-3l-2-2H9V9h2l1-2V4.3a8 8 0 0 1 5.9 13.1z"/></svg>
      www.brinmoretech.example
    </li>
  </ul>

  <div class="person">
    <div class="person-name">Daniel Hale</div>
    <div class="person-title">Founder</div>
  </div>
</section>

</body>
</html>
```